Harlow Mailbox Services, full-service collaboration with postal service - installation of units

1. CBU - Cluster Box Unit - These are Mailbox units that you would see at residential neighborhoods, and Apartments -
2. Logo Needed
3. Maybe have CBU as a division of DWFS (Dermot Vance Field Services)
4. Card to be primary Harlow Mailbox Services

This is a letter of introduction that I am developing:

I am writing to introduce Dermot Vance Field Services, a company dedicated to delivering exceptional service and quality in the installation and maintenance of commercial mailboxes, specifically Cluster Box Units (CBUs). Our commitment to excellence and customer satisfaction has established us as a trusted partner for developers and postal services alike.
At Dermot Vance Field Services, we take pride in our comprehensive approach, ensuring that every step of the mailbox installation process is handled with precision and care. Our services include:
• Supplying high-quality CBUs tailored to meet the specific needs of your development.
• Providing a CBU plat layout upon approval of the address plat, ensuring seamless integration into your development plans.
• Collaborating with developers and postmasters to determine the optimal CBU locations for efficient mail delivery.
• Qualifying the labeling of CBU units, offering both sticker and etching options to suit your preferences.
• Pouring durable concrete foundations as required for the secure installation of the CBU units.
• Handling the installation process with expertise and attention to detail.
• Labeling the units and supplying keys for each mailbox, ensuring a smooth transition for residents and businesses.
Our team is dedicated to working closely with you to ensure that all requirements are met and that the installation process is completed efficiently and to the highest standards.
We look forward to the opportunity to collaborate with you and contribute to the success of your project. Please do not hesitate to contact us for any additional information or to discuss your specific requirements.
Sincerely,
Dermot Vance
Dermot Vance Field Services

Target Market(s)

Developers, Builders, Apartment's, HOA

Industry/Entity Type

Construction

Contact Information for Business Card

Name: Dermot Vance, Cell:555-671-0148, Email: derm@dvfieldco.example

Font styles to use
Serif

Requirements
Must have
• Fresh Looking
Nice to have
• Maybe a CBU Box if it looks clean
Should not have
• Not Industrial or Old traditional card

```html
<!DOCTYPE html>
<html lang="en">
<head>
<meta charset="utf-8">
<title>Harlow Mailbox Services – Business Card</title>
<link href="https://fonts.googleapis.com/css2?family=Lora:wght@400;600;700&display=swap" rel="stylesheet">
<style>
  :root {
    --brand: #86142b;
    --paper: #ffffff;
    --backdrop: #b3b3b3;
    --ink: #1c1c1c;
  }
  * { margin: 0; padding: 0; box-sizing: border-box; }
  html, body { width: 1200px; height: 1200px; overflow: hidden; }
  body {
    background: var(--backdrop);
    position: relative;
    font-family: "Lora", serif;
  }
  .card {
    position: absolute;
    left: 154px;
    width: 892px;
    height: 522px;
    background: var(--paper);
    box-shadow: 10px 12px 14px rgba(0,0,0,0.28);
  }
  .card--front { top: 56px; }
  .card--back { top: 621px; }

  .wordmark {
    position: absolute;
    display: flex;
    align-items: center;
    color: var(--brand);
    font-weight: 600;
    white-space: nowrap;
  }
  .wordmark__square { background: var(--brand); flex: none; }
  .wordmark__text { display: flex; flex-direction: column; line-height: 1; }
  .wordmark__name { font-weight: 700; letter-spacing: 0.5px; }
  .wordmark__sub { font-weight: 600; letter-spacing: 4px; }

  .card--front .wordmark { left: 200px; top: 88px; gap: 20px; }
  .card--front .wordmark__square { width: 104px; height: 104px; }
  .card--front .wordmark__name { font-size: 37px; }
  .card--front .wordmark__sub { font-size: 22px; margin-top: 12px; }

  .card--back .wordmark { left: 142px; top: 195px; gap: 26px; }
  .card--back .wordmark__square { width: 130px; height: 130px; }
  .card--back .wordmark__name { font-size: 45px; }
  .card--back .wordmark__sub { font-size: 27px; margin-top: 15px; }

  .holder-name {
    position: absolute;
    top: 304px;
    left: 0;
    width: 100%;
    text-align: center;
    font-size: 44px;
    line-height: 1;
    font-weight: 700;
    color: var(--brand);
  }
  .contact-band {
    position: absolute;
    left: 0;
    top: 400px;
    width: 446px;
    height: 79px;
    background: var(--brand);
  }
  .contact {
    position: absolute;
    top: 400px;
    height: 79px;
    display: flex;
    align-items: center;
    gap: 18px;
    font-size: 24px;
    font-weight: 400;
    white-space: nowrap;
  }
  .contact--phone { left: 123px; color: var(--paper); letter-spacing: 1px; }
  .contact--email { left: 512px; color: var(--ink); font-size: 23px; }
  .contact svg { width: 32px; height: 32px; flex: none; }
</style>
</head>
<body>

<section class="card card--front">
  <div class="wordmark">
    <span class="wordmark__square"></span>
    <span class="wordmark__text">
      <span class="wordmark__name">HARLOW MAILBOX</span>
      <span class="wordmark__sub">Services, LLC</span>
    </span>
  </div>

  <h1 class="holder-name">Dermot Vance</h1>

  <div class="contact-band"></div>
  <div class="contact contact--phone">
    <svg viewBox="0 0 24 24" aria-hidden="true"><path fill="#ffffff" d="M6.6 10.8a15.2 15.2 0 0 0 6.6 6.6l2.2-2.2a1 1 0 0 1 1-.25 11.4 11.4 0 0 0 3.6.57 1 1 0 0 1 1 1V20a1 1 0 0 1-1 1A17 17 0 0 1 3 4a1 1 0 0 1 1-1h3.5a1 1 0 0 1 1 1c0 1.25.2 2.45.57 3.57a1 1 0 0 1-.25 1z"/></svg>
    <span>555-671-0148</span>
  </div>
  <div class="contact contact--email">
    <svg viewBox="0 0 24 24" aria-hidden="true"><path fill="#86142b" d="M3 5h18a1 1 0 0 1 1 1v12a1 1 0 0 1-1 1H3a1 1 0 0 1-1-1V6a1 1 0 0 1 1-1zm9 7 8-5H4z"/></svg>
    <span>derm@dvfieldco.example</span>
  </div>
</section>

<section class="card card--back">
  <div class="wordmark">
    <span class="wordmark__square"></span>
    <span class="wordmark__text">
      <span class="wordmark__name">HARLOW MAILBOX</span>
      <span class="wordmark__sub">Services, LLC</span>
    </span>
  </div>
</section>

</body>
</html>
```